Hall of Fame announcement social media post

I need a social media Hall of Fame announcement designed in the styles of some of the examples I've posted. I have attached the two gentlemens head shots ... the names are Carl Whitby and Ron Fadley

It is for the TENNESSEE LINKS LEGENDS GALLERY also include 2025 Inductees ... I have also attached the logo... make the post in similar colors as the logo

```html
<!DOCTYPE html>
<html lang="en">
<head>
<meta charset="utf-8">
<title>Tennessee Links Legends Gallery – Class of 2025</title>
<link rel="stylesheet" href="https://fonts.googleapis.com/css2?family=Libre+Caslon+Text:wght@400&family=Figtree:wght@400;500&display=swap">
<style>
  :root {
    --navy: #1f3a6e;
    --red: #d4453a;
    --white: #ffffff;
    --ink: #111111;
    --gold-light: #f7c52a;
    --gold-dark: #c98a12;
    --backdrop-light: #fbfbfb;
    --backdrop-mid: #e6e6e6;
    --portrait-light: #d9d2cc;
    --portrait-dark: #3a3f4a;
  }
  * { margin: 0; padding: 0; box-sizing: border-box; }
  html, body { width: 1200px; height: 1200px; overflow: hidden; background: var(--white); }
  .post {
    position: relative;
    width: 1200px;
    height: 1200px;
    overflow: hidden;
    background: var(--white);
    font-family: "Figtree", sans-serif;
  }
  .backdrop {
    position: absolute;
    left: 0; top: 300px;
    width: 1200px; height: 900px;
    background: radial-gradient(ellipse at 50% 45%, var(--backdrop-mid) 0%, #efefef 45%, var(--backdrop-light) 80%);
  }
  .headline {
    position: absolute;
    top: 130px; left: 0; width: 100%;
    text-align: center;
    font-family: "Libre Caslon Text", serif;
    font-size: 60px;
    font-weight: 400;
    color: var(--ink);
    letter-spacing: -1px;
  }
  .inductee {
    position: absolute;
    top: 400px;
    width: 360px;
    text-align: center;
  }
  .inductee--left { left: 153px; }
  .inductee--right { left: 681px; }
  .portrait { width: 360px; height: 360px; display: block; margin: 0 auto; }
  .inductee-name {
    margin-top: 12px;
    font-family: "Libre Caslon Text", serif;
    font-size: 29px;
    color: var(--ink);
  }
  .accent-star { position: absolute; left: 0; top: 0; width: 1200px; height: 1200px; }
  .class-band {
    position: absolute;
    left: 22px; top: 867px;
    width: 1065px; height: 227px;
    background: var(--navy);
    color: var(--white);
  }
  .band-stripe {
    position: absolute;
    top: 867px; height: 227px;
    background: var(--navy);
  }
  .band-stripe--thin { left: 1108px; width: 12px; }
  .band-stripe--wide { left: 1139px; width: 35px; }
  .gallery-mark {
    position: absolute;
    left: 186px; top: 30px;
    width: 270px;
    text-align: center;
    font-size: 25px;
    font-weight: 500;
    line-height: 1.22;
    letter-spacing: 1px;
    color: var(--white);
  }
  .gallery-year { margin-top: 8px; }
  .inductee-list {
    position: absolute;
    left: 489px; top: 24px;
    list-style: none;
    font-size: 38px;
    line-height: 45.5px;
  }
  .inductee-list li { display: flex; }
  .inductee-list .member { width: 306px; }
</style>
</head>
<body>
<main class="post">
  <div class="backdrop" role="img" aria-label="Softly blurred clubhouse interior behind the inductees"></div>

  <h1 class="headline">Welcome to the Hall.</h1>

  <figure class="inductee inductee--left">
    <svg class="portrait" viewBox="0 0 360 360">
      <defs>
        <linearGradient id="ring-gold-a" x1="0" y1="0" x2="1" y2="1">
          <stop offset="0" stop-color="var(--gold-dark)"/>
          <stop offset="0.5" stop-color="var(--gold-light)"/>
          <stop offset="1" stop-color="var(--gold-dark)"/>
        </linearGradient>
        <linearGradient id="portrait-tone-a" x1="0" y1="0" x2="0" y2="1">
          <stop offset="0" stop-color="var(--portrait-light)"/>
          <stop offset="1" stop-color="var(--portrait-dark)"/>
        </linearGradient>
      </defs>
      <circle cx="180" cy="178" r="163" fill="url(#portrait-tone-a)" role="img" aria-label="Head-and-shoulders portrait of Ron Fadley in a dark suit"/>
      <circle cx="180" cy="178" r="163" fill="none" stroke="url(#ring-gold-a)" stroke-width="9"/>
    </svg>
    <figcaption class="inductee-name">Ron Fadley</figcaption>
  </figure>

  <figure class="inductee inductee--right">
    <svg class="portrait" viewBox="0 0 360 360">
      <defs>
        <linearGradient id="ring-gold-b" x1="0" y1="0" x2="1" y2="1">
          <stop offset="0" stop-color="var(--gold-dark)"/>
          <stop offset="0.5" stop-color="var(--gold-light)"/>
          <stop offset="1" stop-color="var(--gold-dark)"/>
        </linearGradient>
        <linearGradient id="portrait-tone-b" x1="0" y1="0" x2="0" y2="1">
          <stop offset="0" stop-color="var(--portrait-light)"/>
          <stop offset="1" stop-color="var(--portrait-dark)"/>
        </linearGradient>
      </defs>
      <circle cx="180" cy="178" r="163" fill="url(#portrait-tone-b)" role="img" aria-label="Head-and-shoulders portrait of Carl Whitby in a dark suit"/>
      <circle cx="180" cy="178" r="163" fill="none" stroke="url(#ring-gold-b)" stroke-width="9"/>
    </svg>
    <figcaption class="inductee-name">Carl Whitby</figcaption>
  </figure>

  <svg class="accent-star" viewBox="0 0 1200 1200" aria-hidden="true">
    <polygon points="0,794 50,947 217,947 78,1050 128,1194 0,1105" fill="var(--red)"/>
  </svg>

  <section class="class-band">
    <div class="gallery-mark">
      <div>TENNESSEE LINKS</div>
      <div>LEGENDS GALLERY</div>
      <div class="gallery-year">CLASS OF 2025</div>
    </div>
    <ul class="inductee-list">
      <li><span class="member">Evan Bratcher</span><span class="role">Player</span></li>
      <li><span class="member">Rob Halvers</span><span class="role">Coach</span></li>
      <li><span class="member">Martin Mulvey</span><span class="role">Coach</span></li>
      <li><span class="member">Buck Sheffler</span><span class="role">Player</span></li>
    </ul>
  </section>
  <div class="band-stripe band-stripe--thin"></div>
  <div class="band-stripe band-stripe--wide"></div>
</main>
</body>
</html>
```